Business Cards for a law firm

Business cards for our law firm. Use our silhoette logo and OAK HARBOR - check our website (www.oakharbor-legal.com)

Contact Information for Business Card

our silhouette logo, OAK HARBOR, 800-555-0147, Dorian Kestrup, dorian@oakharbor-legal.com

Requirements
Must have
• our silhouette logo, OAK HARBOR, 800-555-0147, Dorian Kestrup, dorian@oakharbor-legal.com

```html
<!DOCTYPE html>
<html lang="en">
<head>
<meta charset="utf-8">
<title>Oak Harbor – Business Cards</title>
<link href="https://fonts.googleapis.com/css2?family=Montserrat:wght@400;600;700&display=swap" rel="stylesheet">
<style>
  :root {
    --navy: #1f3470;
    --ink: #222222;
    --paper: #ffffff;
    --backdrop: #ffffff;
  }
  * { box-sizing: border-box; margin: 0; padding: 0; }
  html, body {
    width: 1200px;
    height: 1000px;
    overflow: hidden;
    background: var(--backdrop);
    font-family: "Montserrat", sans-serif;
    color: var(--navy);
  }
  .canvas { position: relative; width: 1200px; height: 1000px; }
  .card {
    position: absolute;
    left: 367px;
    width: 467px;
    height: 285px;
    background: var(--paper);
    border: 1px solid var(--ink);
    border-radius: 13px;
  }
  .card--front { top: 167px; }
  .card--back { top: 548px; }

  .brand {
    position: absolute;
    display: flex;
    align-items: center;
    gap: 10px;
  }
  .brand__mark {
    width: 46px;
    height: 46px;
    background: var(--navy);
  }
  .brand__name {
    font-weight: 600;
    font-size: 23px;
    letter-spacing: 0.09em;
    color: var(--navy);
    white-space: nowrap;
  }
  .card--front .brand { left: 34px; top: 27px; }
  .card--back .brand { left: 74px; top: 113px; }

  .divider {
    position: absolute;
    left: 24px;
    right: 25px;
    top: 100px;
    height: 1px;
    background: var(--ink);
  }
  .contact {
    position: absolute;
    right: 45px;
    top: 144px;
    text-align: right;
  }
  .contact__name {
    font-weight: 700;
    font-size: 24px;
    line-height: 30px;
    margin-bottom: 6px;
  }
  .contact__line {
    font-weight: 400;
    font-size: 18px;
    line-height: 31px;
  }
</style>
</head>
<body>
<main class="canvas">
  <section class="card card--front" aria-label="Business card front">
    <div class="brand">
      <span class="brand__mark" aria-hidden="true"></span>
      <span class="brand__name">OAK HARBOR</span>
    </div>
    <div class="divider"></div>
    <div class="contact">
      <p class="contact__name">Dorian Kestrup</p>
      <p class="contact__line">800-555-0147</p>
      <p class="contact__line">dorian@oakharbor-legal.com</p>
    </div>
  </section>

  <section class="card card--back" aria-label="Business card back">
    <div class="brand">
      <span class="brand__mark" aria-hidden="true"></span>
      <span class="brand__name">OAK HARBOR</span>
    </div>
  </section>
</main>
</body>
</html>
```